TLR Property - Business Cards

Looking for a business card & general letterhead, signage etc design for our new logo.

Colours:
000a20
0056a2
00b5ef
0088ce
68cef2

Fonts:
Poppins
Karla

Please keep look and feel of new brand - example in the zip package I sent.

```html
<!DOCTYPE html>
<html lang="en">
<head>
<meta charset="utf-8">
<title>TLR Property – Business Cards</title>
<link rel="stylesheet" href="https://fonts.googleapis.com/css2?family=Karla:wght@400;500&family=Poppins:wght@400;500;600;700&display=swap">
<style>
  :root {
    --navy: #000a20;
    --card-navy: #0d1229;
    --royal: #0056a2;
    --sky: #00b5ef;
    --azure: #0088ce;
    --ice: #68cef2;
    --paper: #ffffff;
    --ink-grey: #6b6f78;
    --backdrop: #1e1f23;
  }
  * { box-sizing: border-box; margin: 0; padding: 0; }
  html, body { width: 1200px; height: 952px; overflow: hidden; }
  body {
    background: var(--backdrop);
    display: flex;
    align-items: center;
    justify-content: center;
    gap: 40px;
  }
  .card {
    width: 540px;
    height: 309px;
    position: relative;
    overflow: hidden;
    box-shadow: 0 12px 30px rgba(0,0,0,.45);
  }
  /* Front: contact side */
  .card-front { background: var(--paper); }
  .corner-block {
    position: absolute;
    left: 0; top: 30px;
    width: 34px; height: 40px;
    background: var(--royal);
  }
  .identity { position: absolute; left: 52px; top: 30px; }
  .person-name {
    font-family: "Poppins", sans-serif;
    font-size: 27px;
    line-height: 1.05;
    letter-spacing: .5px;
    text-transform: uppercase;
  }
  .first-name { color: var(--sky); font-weight: 400; }
  .last-name { color: var(--royal); font-weight: 700; }
  .person-role {
    font-family: "Karla", sans-serif;
    font-size: 15px;
    color: var(--ink-grey);
    margin-top: 4px;
  }
  .contact-list {
    list-style: none;
    position: absolute;
    left: 30px; top: 128px;
    font-family: "Karla", sans-serif;
    font-size: 13px;
    color: var(--ink-grey);
    line-height: 1.35;
  }
  .contact-list li { display: flex; align-items: flex-start; gap: 8px; margin-bottom: 6px; }
  .contact-icon {
    width: 17px; height: 17px;
    border-radius: 3px;
    flex: none;
    display: flex; align-items: center; justify-content: center;
  }
  .contact-icon.is-royal { background: var(--royal); }
  .contact-icon.is-sky { background: var(--sky); }
  .contact-icon svg { width: 11px; height: 11px; }

  /* Back: brand side */
  .card-back {
    background: var(--card-navy);
    display: flex;
    align-items: center;
    justify-content: center;
    gap: 14px;
  }
  .brand-dot {
    width: 22px; height: 22px;
    border-radius: 50%;
    background: var(--azure);
  }
  .brand-name {
    font-family: "Poppins", sans-serif;
    font-weight: 600;
    font-size: 40px;
    color: var(--paper);
    letter-spacing: 1px;
  }
</style>
</head>
<body>
  <section class="card card-front" aria-label="Business card front">
    <div class="corner-block"></div>
    <div class="identity">
      <h1 class="person-name"><span class="first-name">Daniel M.</span> <span class="last-name">Harlow</span></h1>
      <p class="person-role">Managing Director</p>
    </div>
    <ul class="contact-list">
      <li>
        <span class="contact-icon is-royal">
          <svg viewBox="0 0 12 12"><path d="M6 1a3.5 3.5 0 0 0-3.5 3.5C2.5 7 6 11 6 11s3.5-4 3.5-6.5A3.5 3.5 0 0 0 6 1zm0 4.8a1.3 1.3 0 1 1 0-2.6 1.3 1.3 0 0 1 0 2.6z" fill="#fff"/></svg>
        </span>
        <span>2715 Lakeview Avenue<br>Portland, OR 97205</span>
      </li>
      <li>
        <span class="contact-icon is-sky">
          <svg viewBox="0 0 12 12"><path d="M3 1.2l1.6 2.2-.9 1.1a6 6 0 0 0 3.8 3.8l1.1-.9L10.8 9 9.6 10.7C5 10.4 1.6 7 1.3 2.4z" fill="#fff"/></svg>
        </span>
        <span>+00 987 654 32</span>
      </li>
      <li>
        <span class="contact-icon is-sky">
          <svg viewBox="0 0 12 12"><rect x="1.5" y="3" width="9" height="6" fill="none" stroke="#fff" stroke-width="1.1"/><path d="M1.5 3L6 6.6 10.5 3" fill="none" stroke="#fff" stroke-width="1.1"/></svg>
        </span>
        <span>contact@tlrproperty.com</span>
      </li>
      <li>
        <span class="contact-icon is-sky">
          <svg viewBox="0 0 12 12"><circle cx="6" cy="6" r="4.4" fill="none" stroke="#fff" stroke-width="1.1"/><path d="M1.6 6h8.8M6 1.6c-2.2 2.6-2.2 6.2 0 8.8M6 1.6c2.2 2.6 2.2 6.2 0 8.8" fill="none" stroke="#fff" stroke-width=".9"/></svg>
        </span>
        <span>www.tlrproperty.com</span>
      </li>
    </ul>
  </section>

  <section class="card card-back" aria-label="Business card back">
    <span class="brand-dot"></span>
    <span class="brand-name">TLR Property</span>
  </section>
</body>
</html>
```